Dietitian needs awesome business card

I need a contemporary design that's eye catching but professional.
My card is to given to doctors, specialists and patients alike.
I manage patients with chronic diseases
I have uploaded my logo and current business card, I would also like the other Registered Clinical Nutritionist logo incorporated into the design

Target Market(s)

Doctors, specialists and patients

Industry/Entity Type

Healthcare

Contact Information for Business Card

www.brindlecovenutrition.com.au
Ph: 0427 516 903
Fax: 6482 7315
email: marcus.k.wellfare@quorvamail.com
Space on the back of the card with: Appointment date, Appointment time and appointment location

Font styles to use
Serif

Colors
fbee3e
876aae
ffc214

Requirements
Must have
• My Logo
• Registered Clinical Nutritionist Logo
• My 4 locations - Fernhollow Medical Centre, North Kelby Health, Ashcourt Medical, Pinebrook Doctors Surgery
Nice to have
• I like the colours in my current business card

```html
<!DOCTYPE html>
<html lang="en">
<head>
<meta charset="utf-8">
<title>Brindlecove Nutrition &amp; Dietetics – Business Card</title>
<link rel="stylesheet" href="https://fonts.googleapis.com/css2?family=Lora:wght@400;500;600&family=Montserrat:wght@400;500;600&display=swap">
<style>
  :root {
    --bg: #2a2a2c;
    --card: #ffffff;
    --green: #3fb34a;
    --navy: #2a3a8f;
    --blue: #2d4fa0;
    --orange: #f47a22;
    --white: #ffffff;
  }
  * { box-sizing: border-box; margin: 0; padding: 0; }
  html, body { width: 1200px; height: 900px; overflow: hidden; background: var(--bg); }
  .canvas { position: relative; width: 1200px; height: 900px; }

  .card {
    position: absolute; width: 680px; height: 390px;
    background: var(--card); border-radius: 26px; overflow: hidden;
    box-shadow: 0 14px 30px rgba(0,0,0,.45);
  }
  .card--back { left: 100px; top: 50px; }
  .card--front { left: 420px; top: 460px; }

  .brand { position: absolute; display: flex; align-items: center; gap: 14px; }
  .brand__dot { width: 62px; height: 62px; border-radius: 50%; background: var(--green); flex: none; }
  .brand__name {
    font-family: "Lora", serif; font-weight: 500; color: var(--blue);
    line-height: 1.05; font-size: 34px;
  }
  .brand__name small { display: block; font-size: 19px; }
  .card--back .brand { left: 44px; top: 56px; }
  .card--front .brand { left: 30px; top: 200px; }
  .card--front .brand__name { font-size: 30px; }
  .card--front .brand__name small { font-size: 16px; }

  .appointment { position: absolute; left: 44px; top: 156px; right: 40px; font-family: "Montserrat", sans-serif; }
  .appointment__title { color: var(--green); font-weight: 600; font-size: 20px; margin-bottom: 14px; }
  .field { display: flex; align-items: flex-end; gap: 8px; color: var(--navy); font-size: 16px; margin-bottom: 18px; }
  .field__line { flex: 1; border-bottom: 1.5px solid var(--navy); height: 18px; }
  .field__label { white-space: nowrap; }
  .credentials {
    position: absolute; left: 44px; bottom: 60px;
    font-family: "Lora", serif; color: var(--navy); font-size: 19px;
  }
  .locations {
    position: absolute; left: 44px; right: 36px; bottom: 30px;
    font-family: "Montserrat", sans-serif; font-weight: 500; color: var(--green);
    font-size: 12px; white-space: nowrap;
  }

  .front-panel { position: absolute; inset: 0; }
  .contact { position: absolute; left: 372px; top: 104px; color: var(--white); }
  .contact__name { font-family: "Lora", serif; font-weight: 500; font-size: 29px; margin-bottom: 14px; }
  .contact__list { list-style: none; font-family: "Montserrat", sans-serif; font-size: 15px; }
  .contact__list li { display: flex; align-items: center; gap: 10px; margin-bottom: 6px; }
  .contact__list svg { width: 13px; height: 13px; flex: none; }
  .membership { position: absolute; right: 26px; bottom: 36px; width: 150px; height: 76px; }
</style>
</head>
<body>
<main class="canvas">

  <section class="card card--back" aria-label="Appointment side">
    <div class="brand">
      <span class="brand__dot"></span>
      <p class="brand__name">Brindlecove<small>Nutrition &amp; Dietetics</small></p>
    </div>
    <div class="appointment">
      <p class="appointment__title">Appointment:</p>
      <div class="field"><span class="field__label">Date:</span><span class="field__line"></span><span class="field__label">Time:</span><span class="field__line"></span></div>
      <div class="field"><span class="field__label">Location:</span><span class="field__line"></span></div>
    </div>
    <p class="credentials">Registered Clinical Nutritionist, Nutritionist and Chef</p>
    <p class="locations">Fernhollow Medical Centre · North Kelby Health · Ashcourt Medical · Pinebrook Doctors Surgery</p>
  </section>

  <section class="card card--front" aria-label="Contact side">
    <svg class="front-panel" viewBox="0 0 680 390" preserveAspectRatio="none" aria-hidden="true">
      <polygon points="272,0 680,0 680,390 408,390 331,170 312,160 321,140" fill="#3fb34a"/>
      <polyline points="266,0 315,140 305,160 325,170 402,390" fill="none" stroke="#2a3a8f" stroke-width="2"/>
    </svg>
    <div class="brand">
      <span class="brand__dot"></span>
      <p class="brand__name">Brindlecove<small>Nutrition &amp; Dietetics</small></p>
    </div>
    <div class="contact">
      <p class="contact__name">Marcus Wellfare</p>
      <ul class="contact__list">
        <li><svg viewBox="0 0 16 16"><path d="M4 1l3 3-2 2a9 9 0 005 5l2-2 3 3-2 3C7 15 1 9 1 3z" fill="#fff"/></svg>0427 516 903</li>
        <li><svg viewBox="0 0 16 16"><rect x="2" y="5" width="12" height="8" rx="1" fill="#fff"/><rect x="4" y="1" width="8" height="4" fill="#fff"/></svg>6482 7315</li>
        <li><svg viewBox="0 0 16 16"><rect x="1.5" y="3.5" width="13" height="9" fill="none" stroke="#fff" stroke-width="1.5"/><path d="M2 4l6 5 6-5" fill="none" stroke="#fff" stroke-width="1.5"/></svg>marcus.k.wellfare@quorvamail.com</li>
        <li><svg viewBox="0 0 16 16"><circle cx="8" cy="8" r="6.5" fill="none" stroke="#fff" stroke-width="1.5"/><path d="M1.5 8h13M8 1.5c-3 3.5-3 9.5 0 13M8 1.5c3 3.5 3 9.5 0 13" fill="none" stroke="#fff" stroke-width="1.2"/></svg>www.brindlecovenutrition.com.au</li>
      </ul>
    </div>
    <svg class="membership" viewBox="0 0 150 76" role="img" aria-label="Membership badge">
      <rect width="150" height="76" fill="#f47a22" stroke="#fff" stroke-width="2"/>
      <circle cx="116" cy="30" r="20" fill="#fff"/>
    </svg>
  </section>

</main>
</body>
</html>
```